Specialist Executive Search firm needs new MS Word template(and other templates to match eventually)

Corvel Associates a boutique Executive Search and Recruitment firm, recruiting senior specialist advisors in the fields of Audit, Advisory, Tax Accounting, Corporate Finance and Law. The majority of our clients are professional services firms, i.e. Accounting firms and Law firms.

The ‘Research List / Market Map’ document we currently use to produce and then present to clients is a "long list" of candidates or prospective target candidates. It is a bit dated, and the formatting can be fiddly. So we would like someone to freshen it up and simplify it so that is functions much more effectively as a usable, consistent Template and it needs to be in MS Word. We are looking for something simple and contemporary, but professional, given the nature of our clients - usually Managing Partners or very Senior Partners - in Accounting and Law firms. We need it to be easy to use, so that we can just copy and paste information into it without the formatting requiring constant adjustment and checking.

The "usual" sequence of the document:

- Cover page - includes the name of the company we are sending it to, the role we are recruiting for, and a sketch of the city the role is in (or similar other sketch). The Corvel Associates brand is also featured.
- Confidentiality summary page,
- Table of contents - we would like this to be automated so that page numbers adjusted automatically to be accurate with contents page
- Project summary - usually 1 to 2 pages summarising the purpose of the project and the content of the document
- "Highlighted Candidates" page, which are targets / candidates we think are likely of particular interest to our client.
- Then a page or number of pages (depending on the nature of the search, this is sometimes up to 5 to 6 pages for each and every firm….with an average of 3/4 individuals per page. Other times, it may be just one individual per employer/firm) listed by firm with the following details of each candidate:
- Photo of target individual
- Name of individual
- Job title
- Location
- Summary of the individual and their experience, which can be between 1-2 paragraphs.

We are open to suggestions with respect to the above, i.e. improved format / layout / order of information.

We currently group target candidates by the firm that currently employs each. Each firm has the heading and we like them grouped this way, as do our clients as it assists with seeking feedback / market information from various stakeholders inside the client. We tend to group very large firms (TbR, LHNQ, Varnsby, QO) at the beginning of each market document, followed by large international mid tier firms, followed by quality boutiques and smaller firms. Whilst it can vary somewhat, generally speaking the larger firms are comprised of a larger number of potential targets than smaller firms. For obvious reasons.

I have attached an example of what we currently have, but please bear in mind this is a mock up for confidentiality reasons. I haven't included the confidentiality summary page, or the project summary either. Ideally for integration purposes, and to make it simpler to copy data from our CRM system and paste into the document, there will be a hidden table for the candidate information.

We also want a new font, as the one we have (DIN) needs to be downloaded by each user and if we send the document in MS Word format, the formatting can be totally unreadable to the recipient or at the very least can impact the layout and format. So perhaps a simple font that we can use as part of our brand, but that still looks smart and contemporary.

Once we finalise this word template, we will need to match it with our other proposal documents, terms of business, powerpoint templates etc, and we also need to refresh/redo our website.

I only work two days per week so it's a long time between me reviewing designs, and discussing with the Partners of the business.

Target Market(s)

Professional services firms, Director and Partner level

Industry/Entity Type

Recruitment

Font styles to use
Other font styles liked:
• Currently use DIN but keen for a different signature font to suit

Requirements
Must have
• Must be simple to copy and paste text from our other system, and our business colours which are dark brown and dark red - RGB codes to come shortly

```html
<!DOCTYPE html>
<html lang="en">
<head>
<meta charset="utf-8">
<title>Corvel Associates – Market Map Template</title>
<link href="https://fonts.googleapis.com/css2?family=Poppins:wght@400;600;700&family=Questrial&display=swap" rel="stylesheet">
<style>
:root{
  --red:#d22a2a;
  --red-dark:#9e1f1f;
  --brown:#4a1712;
  --grey:#b5b5b5;
  --ink:#3a3a3a;
  --muted:#8a8a8a;
  --stage:#c6c6c6;
  --night:#1b1c22;
}
*{box-sizing:border-box;margin:0;padding:0}
html,body{width:1200px;height:4205px;overflow:hidden;background:#fff}
body{position:relative;font-family:"Questrial",sans-serif;color:var(--ink)}
.stage{position:absolute;left:0;top:0;width:1200px;height:800px;background:var(--stage)}
.page{position:absolute;width:425px;height:614px;background:#fff;box-shadow:0 0 4px rgba(0,0,0,.18);overflow:hidden}
.pnum{position:absolute;top:10px;right:14px;font-size:5px;color:var(--muted)}
.inner{position:absolute;left:34px;right:34px;top:34px}
.title{font:600 17px "Poppins",sans-serif;color:var(--red);margin-bottom:12px;letter-spacing:.1px}
.body{font-size:5.3px;line-height:1.4;color:var(--ink)}
.body p{margin-bottom:4px}
.red{color:var(--red)}
.foot{position:absolute;left:34px;right:34px;bottom:12px;border-top:.5px solid #e2e2e2;padding-top:5px;display:flex;justify-content:space-between;align-items:flex-end}
.foot .cities{font-size:4.3px;color:var(--muted);line-height:1.4}
.foot .cities span{color:var(--red)}
.brand{font:700 9px "Poppins",sans-serif;color:var(--brown);display:flex;align-items:baseline;gap:4px}
.brand small{font:400 3.8px "Questrial",sans-serif;color:var(--red)}
/* cover */
.cover .art{position:absolute;left:0;top:0;width:100%;height:375px;background:linear-gradient(180deg,#f3e9ea 0%,#e6ccd0 55%,#c99aa0 100%)}
.cover .band{position:absolute;left:0;top:375px;width:100%;height:160px;background:linear-gradient(180deg,#d83131,#c52525);padding:22px 46px;color:#fff}
.cover h1{font:600 20px/1.3 "Poppins",sans-serif}
.cover .date{font-size:9px;margin:10px 0 6px}
.cover .lede{font-size:7.6px;line-height:1.35}
.cover .base{position:absolute;left:0;top:535px;width:100%;height:79px;background:linear-gradient(180deg,#7a5a52,#5a4a48)}
.cover .brand{position:absolute;right:14px;bottom:14px;color:#fff;font-size:13px}
/* toc */
.toc{font-size:7.4px;line-height:1.3}
.toc .grp{color:var(--red);margin-top:10px}
.toc .row{display:flex;justify-content:space-between;padding-left:15px}
/* headings list */
.h1{color:var(--red);font-size:9px;margin:4px 0}
.h2{color:var(--red);font-size:7.8px;margin:4px 0 3px 12px}
.h3{color:var(--red);font-size:6.4px;margin:3px 0 3px 24px}
.h4{color:var(--red);font-size:6px;margin:3px 0 3px 36px}
.h5{color:var(--red);font-size:6px;margin:3px 0 3px 48px}
.ind1{margin-left:12px}.ind2{margin-left:24px}.ind3{margin-left:36px}.ind4{margin-left:48px}.ind5{margin-left:60px}
ol.num{padding-left:10px}
ol.num li{margin-bottom:4px}
/* summary */
.kicker{font-size:7px;letter-spacing:.3px;margin-bottom:8px}
.item{display:flex;gap:8px;margin-bottom:8px}
.ico{flex:0 0 17px;height:17px;border:1.3px solid var(--red);border-radius:50%}
.item h3{font:400 8px "Questrial",sans-serif;color:var(--red);margin-bottom:2px}
.item ul{list-style:disc;padding-left:10px}
.grid{display:grid;grid-template-columns:repeat(4,1fr);gap:0 4px;font-size:4.4px;line-height:1.35}
.grid .hd{background:var(--red);color:#fff;font-size:6px;padding:2px 3px}
.grid .c{padding:3px 3px 3px 8px}
.grid .c.alt{background:#eee}
.grid ul{list-style:disc}
/* candidate */
.cand{display:flex;gap:10px}
.photo{flex:0 0 80px;height:86px;background:linear-gradient(160deg,#d8d8d8,#8c8c8c)}
.name{font:400 9px "Questrial",sans-serif;color:var(--red)}
.badge{display:inline-block;background:var(--red);color:#fff;font-size:5.5px;padding:1px 4px;margin:2px 0 4px}
.contact{font-size:4.6px;display:flex;gap:10px;margin-bottom:4px}
.contact span::before{content:"";display:inline-block;width:4px;height:4px;border-radius:50%;background:var(--red);margin-right:2px;vertical-align:middle}
.exp-h{font-size:7.5px;color:var(--red);margin:10px 0 6px}
.tl{position:relative;padding-left:18px}
.tl::before{content:"";position:absolute;left:5px;top:3px;bottom:10px;border-left:.7px solid var(--red)}
.tl .yr{position:relative;color:var(--red);font-size:7px}
.tl .yr::before{content:"";position:absolute;left:-16px;top:1px;width:6px;height:6px;border-radius:50%;background:var(--red)}
.tl .ct{font-size:6.2px;margin:2px 0 1px}
.tl .tx{font-size:5px;line-height:1.4;margin-bottom:7px}
.tl ul{padding-left:8px}
/* dark */
.dark{background:var(--night)}
.dark .body{color:#d5d5d5}
.dark .foot{border-color:#444}
.dark .brand{color:#fff}
.dark ul{padding-left:10px}
/* image page */
.photo-wide{width:100%;height:165px;background:linear-gradient(180deg,#8d8c92 0%,#b9aba0 45%,#b88a55 75%,#6b5740 100%);margin-bottom:10px}
.quote{display:flex;gap:8px;font-size:9.5px;line-height:1.3;color:var(--ink);margin-top:14px}
.qm{font:700 26px/1 "Poppins",sans-serif;color:var(--red)}
.qm-end{display:block;text-align:right;font:700 26px/1 "Poppins",sans-serif;color:var(--red);margin-top:2px}
/* thank you */
.thanks{background:linear-gradient(180deg,#d23030,#c02525);color:#fff;text-align:center}
.thanks .glow{position:absolute;left:110px;top:90px;width:205px;height:470px;background:radial-gradient(ellipse at 50% 40%,rgba(255,255,255,.16),rgba(255,255,255,0) 70%)}
.thanks h2{position:absolute;top:222px;width:100%;font:700 27px "Poppins",sans-serif;letter-spacing:.5px}
.thanks .brand{position:absolute;top:450px;width:100%;justify-content:center;color:#fff;font-size:17px}
.thanks .cities{position:absolute;top:477px;width:100%;font-size:5px;line-height:1.4}
</style>
</head>
<body>

<div class="stage">
  <section class="page" style="left:163px;top:93px">
    <div class="pnum">8</div>
    <div class="inner">
      <h2 class="title">Highlighted Candidates</h2>
      <div class="cand">
        <div class="photo" role="img" aria-label="Portrait photo of candidate"></div>
        <div class="body">
          <div class="name">John Doe</div>
          <div class="badge">Vice President</div>
          <div class="contact"><span>United Kingdom</span><span>info@corvelassociates.co.uk</span><span>+44 200 000 0000</span></div>
          <p>Lorem ipsum dolor sit amet, consectetur adipiscing elit. Vivamus sed ullamcorper libero. Nam cursus ut turpis eu porttitor. Duis sit amet neque ultrices, aliquet mauris non, pulvinar augue. Aenean tellus mi, fermentum in pharetra vitae, semper a est.</p>
          <p>Quisque et pulvinar urna, ut pretium leo. Mauris turpis quam, bibendum at risus in, vestibulum accumsan leo. Donec eu convallis neque. Etiam aliquet, dui at gravida posuere.</p>
        </div>
      </div>
      <div class="exp-h">Professional Experience</div>
      <div class="tl">
        <div class="yr">2010</div><div class="ct">Content Here</div>
        <div class="tx">Lorem ipsum dolor sit amet, consectetur adipiscing elit. Vivamus sed ullamcorper libero. Nam cursus ut turpis eu porttitor.</div>
        <div class="yr">2015</div><div class="ct">Content Here</div>
        <div class="tx"><ul><li>Lorem ipsum dolor sit amet, consectetur adipiscing elit.</li><li>Vivamus sed ullamcorper libero. Nam cursus ut turpis.</li><li>Duis sit amet neque ultrices, aliquet mauris non.</li></ul></div>
        <div class="yr">2018</div><div class="ct">Content Here</div>
        <div class="tx"><ul><li>Fusce rhoncus lectus et augue tincidunt tempor.</li><li>Aenean vestibulum nunc ac diam scelerisque.</li><li>Integer nec felis non neque mattis fermentum.</li><li>Sed egestas et elit placerat commodo at a lorem.</li></ul></div>
        <div class="yr">2018 – Now</div><div class="ct">Content Here</div>
        <div class="tx"><ul><li>Fusce rhoncus lectus et augue tincidunt tempor.</li><li>Aenean vestibulum nunc ac diam scelerisque, et efficitur ligula pharetra.</li></ul></div>
      </div>
    </div>
    <footer class="foot"><div class="cities">London | Dubai | Melbourne | St. Helier | Sydney<br><span>www.corvelassociates.net</span></div><div class="brand">Corvel Associates <small>Executive search &amp; advisory</small></div></footer>
  </section>

  <section class="page cover" style="left:607px;top:93px">
    <div class="art" role="img" aria-label="Pen sketch of the Sydney skyline and opera house in soft red tones"></div>
    <div class="band">
      <h1>Partner Corporate Tax –<br>Sydney Prepared for “Client”</h1>
      <div class="date">9 March 2020</div>
      <div class="lede">Lorem ipsum dolor sit amet, consectetur adipiscing elit. Maecenas porttitor congue massa. Fusce posuere, magna sed pulvinar ultricies, purus lectus.</div>
    </div>
    <div class="base" role="img" aria-label="Harbour foreshore sketch in muted tones"></div>
    <div class="brand">Corvel Associates</div>
  </section>
</div>

<!-- Row 1 -->
<section class="page cover" style="left:163px;top:934px">
  <div class="art" role="img" aria-label="Pen sketch of the Sydney skyline and opera house in soft red tones"></div>
  <div class="band">
    <h1>Partner Corporate Tax –<br>Sydney Prepared for “Client”</h1>
    <div class="date">9 March 2020</div>
    <div class="lede">Lorem ipsum dolor sit amet, consectetur adipiscing elit. Maecenas porttitor congue massa. Fusce posuere, magna sed pulvinar ultricies, purus lectus.</div>
  </div>
  <div class="base" role="img" aria-label="Harbour foreshore sketch in muted tones"></div>
  <div class="brand">Corvel Associates</div>
</section>

<section class="page" style="left:607px;top:934px">
  <div class="pnum">2</div>
  <div class="inner">
    <h2 class="title">Table of Contents</h2>
    <div class="toc">
      <div class="grp">Big 4 Firms</div>
      <div class="row"><span>Varnsby</span><span>7</span></div>
      <div class="row"><span>QO</span><span>9</span></div>
      <div class="row"><span>LHNQ</span><span>10</span></div>
      <div class="row"><span>TbR Group</span><span>11</span></div>
      <div class="grp" style="display:flex;justify-content:space-between"><span>Mid Tier Firms</span><span style="color:var(--ink)">12</span></div>
      <div class="row"><span>Almont</span><span>12</span></div>
      <div class="row"><span>Fairmoor</span><span>15</span></div>
      <div class="row"><span>Castlereigh</span><span>16</span></div>
      <div class="row"><span>Elbury Finch</span><span>17</span></div>
      <div class="row"><span>Ostrand Vale</span><span>18</span></div>
      <div class="row"><span>Penrose Lindqvist</span><span>20</span></div>
      <div class="row"><span>Quarrington Ames</span><span>21</span></div>
      <div class="row"><span>Tessaro + Partners</span><span>23</span></div>
      <div class="row"><span>Brightwater</span><span>24</span></div>
      <div class="row"><span>Solent</span><span>25</span></div>
      <div class="row"><span>Marlowe Partners</span><span>26</span></div>
      <div class="row"><span>JXT</span><span>27</span></div>
      <div class="row"><span>GWL</span><span>28</span></div>
      <div class="row"><span>Ravenhill Doyle</span><span>29</span></div>
      <div class="row"><span>Ashgrove</span><span>30</span></div>
      <div class="row"><span>Other</span><span>31</span></div>
    </div>
  </div>
  <footer class="foot"><div class="cities">London | Dubai | Melbourne | St. Helier | Sydney<br><span>www.corvelassociates.net</span></div><div class="brand">Corvel Associates <small>Executive search &amp; advisory</small></div></footer>
</section>

<!-- Row 2 -->
<section class="page" style="left:163px;top:1566px">
  <div class="pnum">3</div>
  <div class="inner body">
    <h2 class="title">Paragraph Style</h2>
    <div class="h1">1.&nbsp; Nullam id lorem a neque ornare condimentum.</div>
    <p>Lorem ipsum dolor sit amet, consectetur adipiscing elit. Pellentesque tristique tempus turpis, et aliquam est lacinia sit amet. Ut ac eros vel metus gravida varius. Morbi quis tempus dolor. Donec efficitur, tortor nec convallis aliquet, sapien sapien accumsan lorem, nec tristique sem nec nisi tellus.</p>
    <div class="h2">1.1.Nullam id lorem a neque ornare condimentum.</div>
    <p class="ind2">Proin diam odio, elementum sit amet urna sit, venenatis lobortis nisin. Morbi imperdiet ipsum ac interdum dignissim. Nulla mi justo, sagittis et pharetra eget, varius ultricies risus. Etiam accumsan viverra nibh. In eget magna gravida, feugiat nisi et, aliquam sapien. Vivamus in suscipit quam, id condimentum nulla. Aliquam quis porta tellus.</p>
    <div class="h3">1.1.1. Vestibulum pellentesque lorem in orci ultricies ultricies.</div>
    <p class="ind3">Fusce sapien sem, pharetra in sagittis et, mattis quis erat. Maecenas at nisi diam. Aenean blandit risus non quam tincidunt, quis bibendum erat pretium. Praesent tincidunt placerat imperdiet. Duis vitae augue auctor, gravida enim quis, facilisis ligula. Curabitur molestie vehicula faucibus.</p>
    <div class="h4">1.1.1.1. Proin at nisl placerat, suscipit lacus et, tincidunt elit.</div>
    <p class="ind4">Integer cursus, eros sed finibus dapibus, odio urna auctor sem, ac malesuada risus magna at arcu. Interdum et malesuada fames ac ante ipsum primis in faucibus. Donec facilisis semper eleifend. Nulla faucibus eleifend tincidunt. Maecenas id lacinia ipsum. Quisque eget facilisis justo.</p>
    <div class="h5">1.1.1.1.1. Maecenas eu risus id diam porttitor aliquet.</div>
    <p class="ind5">Aliquam id cursus velit, eu porta ligula. Aenean ut massa ligula. Fusce at dolor vehicula, vehicula est ac, faucibus massa. Maecenas id nunc vitae orci congue imperdiet eget quis elit. Etiam sit amet felis sit amet urna pellentesque imperdiet eu ac quam.</p>
  </div>
  <footer class="foot"><div class="cities">London | Dubai | Melbourne | St. Helier | Sydney<br><span>www.corvelassociates.net</span></div><div class="brand">Corvel Associates <small>Executive search &amp; advisory</small></div></footer>
</section>

<section class="page" style="left:607px;top:1566px">
  <div class="pnum">4</div>
  <div class="inner body">
    <h2 class="title">Confidential Information</h2>
    <div class="h1" style="font-size:7.5px">Lorem ipsum adipiscing elit.</div>
    <ol class="num">
      <li>Vivamus sed ullamcorper libero. Nam cursus ut turpis eu porttitor. Duis sit amet neque ultrices, aliquet mauris non, pulvinar augue. Aenean tellus mi, fermentum in pharetra vitae, semper a est. Duis nec auctor eros. Integer ultrices lectus risus, vitae dapibus tortor varius vel.</li>
      <li>Quisque et pulvinar urna, ut pretium leo. Mauris turpis quam, bibendum at risus in, vestibulum accumsan leo. Donec eu convallis neque. Etiam aliquet, dui at gravida posuere, dui mi pellentesque mi, eget lobortis eros justo ac magna. Suspendisse at nunc non risus dictum sodales ut nec mi.</li>
      <li>Donec tempus arcu sed ante lacinia auctor. Fusce sodales maximus fermentum. Cras accumsan convallis volutpat. Nulla in imperdiet diam. Maecenas at odio nisi. Aliquam erat volutpat. Pellentesque sed nulla eu quam pellentesque elementum. Donec sollicitudin efficitur metus.</li>
      <li>Cras faucibus eget quam in hendrerit. Praesent egestas laoreet ex. Praesent pharetra placerat sem non pretium. Aliquam consequat sollicitudin dolor. Etiam metus sapien, consectetur at nisi quis, porttitor tempus arcu. Mauris bibendum leo auctor ligula pulvinar bibendum.</li>
    </ol>
    <div class="h1" style="font-size:7.5px">Integer eget lorem blandit, mollis metus sit amet.</div>
    <p>Pellentesque ut nisl eget tellus dapibus dictum non ut felis. Nulla tortor neque, tempor pretium hendrerit et, molestie a augue. Vivamus at suscipit neque, nec sodales sem. Quisque diam risus, pharetra non bibendum eu, luctus sed ipsum. Pellentesque porta odio dolor, in gravida arcu congue id. Maecenas nulla quam, sagittis vel elit quis, fermentum vulputate nulla. Sed vitae turpis ut diam ornare eu, finibus sagittis leo. Nulla dictum viverra mauris ut dapibus. Aenean ac tristique sem. Suspendisse et dapibus nulla, vel dapibus elit. Integer quis libero non massa lacinia consectetur ac a ex. Praesent eros turpis, tempus sit amet sapien id, fermentum fermentum risus.</p>
    <p>Donec malesuada pellentesque neque. Curabitur vitae neque vel lorem sollicitudin aliquet vel a massa. Suspendisse et magna ac leo tempus posuere eu at lectus. Donec placerat vitae nisl rutrum dapibus. Suspendisse a dolor id magna tincidunt efficitur sed ut nulla. Sed placerat odio ac erat blandit sagittis. Interdum et malesuada fames ac ante ipsum primis in faucibus. Pellentesque ut feugiat tortor. Donec erat libero, sollicitudin a sollicitudin tristique, euismod vitae nulla.</p>
    <p class="red" style="margin-top:14px;font-style:italic;font-weight:bold">Aenean mauris libero,<br>ornare sed placerat vitae, ornare in velit.</p>
  </div>
  <footer class="foot"><div class="cities">London | Dubai | Melbourne | St. Helier | Sydney<br><span>www.corvelassociates.net</span></div><div class="brand">Corvel Associates <small>Executive search &amp; advisory</small></div></footer>
</section>

<!-- Row 3 -->
<section class="page" style="left:163px;top:2195px">
  <div class="pnum">5</div>
  <div class="inner body">
    <h2 class="title">Project Summary</h2>
    <div class="kicker">EXECUTIVE SUMMARY</div>
    <div class="item"><div class="ico"></div><div><h3>Overview - The Quick Pitch</h3><p>This is a brief section that describes what your business or project is all about.</p><p><b>TIP: The ability to describe what your business does in just one compelling sentence will be a huge asset to you as you talk about it with others.</b></p></div></div>
    <div class="item"><div class="ico"></div><div><h3>The Problem</h3><p>Here is where you describe the problem that you are solving.</p><ul><li>What is the problem and how big is it?</li><li>Who is the target audience? Who is this problem affecting?</li><li>Are there currently any solutions to this problem? Who is the competition?</li></ul></div></div>
    <div class="item"><div class="ico"></div><div><h3>The Solution</h3><p>Here you describe how your business solves the problem for your target audience.</p><ul><li>How does your business solve the problem?</li><li>Is it a simple or complex solution?</li><li>If it is complex, how can you make it simpler, or describe it more simply?</li></ul></div></div>
    <div class="item"><div class="ico"></div><div><h3>Highlights</h3><p>Here you can show the most important market analysis and data that captures the potential your solution can have in the marketplace. We recommend putting the most compelling highlights from your plan or proposal. You can also talk about the strengths and advantages of your staff and any partnerships you may have.</p></div></div>
    <svg width="357" height="205" viewBox="0 0 357 205" font-family="Questrial, sans-serif" font-size="6" fill="#3a3a3a" aria-label="Bar chart of four categories">
      <g stroke="#eee" stroke-width=".5">
        <line x1="70" y1="0" x2="70" y2="180"/><line x1="115" y1="0" x2="115" y2="180"/><line x1="160" y1="0" x2="160" y2="180"/><line x1="205" y1="0" x2="205" y2="180"/><line x1="250" y1="0" x2="250" y2="180"/><line x1="295" y1="0" x2="295" y2="180"/><line x1="340" y1="0" x2="340" y2="180"/>
      </g>
      <g text-anchor="end"><text x="64" y="26">Category 4</text><text x="64" y="70">Category 3</text><text x="64" y="114">Category 2</text><text x="64" y="158">Category 1</text></g>
      <g>
        <rect x="70" y="8" width="225" height="6" fill="#d22a2a"/><rect x="70" y="18" width="126" height="6" fill="#4a1712"/><rect x="70" y="28" width="202" height="6" fill="#b5b5b5"/>
        <rect x="70" y="52" width="135" height="6" fill="#d22a2a"/><rect x="70" y="62" width="81" height="6" fill="#4a1712"/><rect x="70" y="72" width="157" height="6" fill="#b5b5b5"/>
        <rect x="70" y="96" width="90" height="6" fill="#d22a2a"/><rect x="70" y="106" width="198" height="6" fill="#4a1712"/><rect x="70" y="116" width="112" height="6" fill="#b5b5b5"/>
        <rect x="70" y="140" width="90" height="6" fill="#d22a2a"/><rect x="70" y="150" width="108" height="6" fill="#4a1712"/><rect x="70" y="160" width="193" height="6" fill="#b5b5b5"/>
      </g>
      <g font-size="5"><text x="298" y="13">5</text><text x="199" y="23">2.8</text><text x="275" y="33">4.5</text><text x="208" y="57">3</text><text x="154" y="67">1.8</text><text x="230" y="77">3.5</text><text x="163" y="101">2</text><text x="271" y="111">4.4</text><text x="185" y="121">2.5</text><text x="163" y="145">2</text><text x="181" y="155">2.4</text><text x="266" y="165">4.3</text></g>
      <g text-anchor="middle"><text x="70" y="192">0</text><text x="115" y="192">1</text><text x="160" y="192">2</text><text x="205" y="192">3</text><text x="250" y="192">4</text><text x="295" y="192">5</text><text x="340" y="192">6</text></g>
    </svg>
  </div>
  <footer class="foot"><div class="cities">London | Dubai | Melbourne | St. Helier | Sydney<br><span>www.corvelassociates.net</span></div><div class="brand">Corvel Associates <small>Executive search &amp; advisory</small></div></footer>
</section>

<section class="page" style="left:607px;top:2195px">
  <div class="pnum">6</div>
  <div class="inner body">
    <h2 class="title">Project Summary</h2>
    <div class="item"><div class="ico"></div><div><h3>Keys to Success</h3><p>Discuss the main steps necessary for your business to be successful.</p><ul><li>What is your marketing strategy?</li><li>What resources will you need? (partnerships, funding, materials)</li><li>What does your timeline look like?</li></ul></div></div>
    <div class="item"><div class="ico"></div><div><h3>Financial Highlights</h3><p>If part of the purpose of your proposal is to seek funding, you may want to dedicate a full section to talk about the funding you currently have and what funding you'll need.</p><ul><li>What is your 3-year earnings projection?</li><li>When will you break even?</li><li>How will investors be repaid?</li></ul></div></div>
    <svg width="357" height="150" viewBox="0 0 357 150" font-family="Questrial, sans-serif" aria-label="Donut chart of quarterly share">
      <g transform="translate(178 65) rotate(-90)" fill="none" stroke-width="22">
        <circle r="40" stroke="#d22a2a" stroke-dasharray="155.8 251.3"/>
        <circle r="40" stroke="#9e1f1f" stroke-dasharray="37.7 251.3" stroke-dashoffset="-155.8"/>
        <circle r="40" stroke="#4a1712" stroke-dasharray="37.7 251.3" stroke-dashoffset="-193.5"/>
        <circle r="40" stroke="#b5b5b5" stroke-dasharray="20.1 251.3" stroke-dashoffset="-231.2"/>
      </g>
      <g fill="#fff" font-size="8" font-weight="bold" text-anchor="middle"><text x="216" y="82">62%</text><text x="147" y="92">15%</text><text x="143" y="58">15%</text><text x="163" y="33">8%</text></g>
      <g font-size="5" fill="#3a3a3a">
        <circle cx="128" cy="139" r="1.5" fill="#d22a2a"/><text x="132" y="141">1st Qtr</text>
        <circle cx="156" cy="139" r="1.5" fill="#9e1f1f"/><text x="160" y="141">2nd Qtr</text>
        <circle cx="186" cy="139" r="1.5" fill="#4a1712"/><text x="190" y="141">3rd Qtr</text>
        <circle cx="214" cy="139" r="1.5" fill="#b5b5b5"/><text x="218" y="141">4th Qtr</text>
      </g>
    </svg>
    <div class="grid" style="margin-top:10px">
      <div class="hd">Lorem ipsum</div><div class="hd">Lorem ipsum 1</div><div class="hd">Lorem ipsum 2</div><div class="hd">Lorem ipsum 3</div>
      <div class="c"><ul><li>Lorem ipsum dolor sit amet, consectetur adipiscing elit.</li><li>Quisque nec enim luctus, finibus</li></ul></div>
      <div class="c"><ul><li>Lorem ipsum dolor sit amet, consectetur adipiscing elit.</li></ul></div>
      <div class="c"><ul><li>Lorem ipsum dolor sit amet, consectetur adipiscing elit.</li></ul></div>
      <div class="c"><ul><li>Lorem ipsum dolor sit amet, consectetur adipiscing elit.</li></ul></div>
      <div class="c alt"><ul><li>Lorem ipsum dolor sit amet, consectetur adipiscing elit.</li></ul></div>
      <div class="c alt"><ul><li>Lorem ipsum dolor sit amet, consectetur adipiscing elit.</li></ul></div>
      <div class="c alt"><ul><li>Lorem ipsum dolor sit amet, consectetur adipiscing elit.</li></ul></div>
      <div class="c alt"><ul><li>Lorem ipsum dolor sit amet, consectetur adipiscing elit.</li><li>Quisque nec enim luctus</li></ul></div>
      <div class="c"><ul><li>Lorem ipsum dolor sit amet, consectetur adipiscing elit.</li></ul></div>
      <div class="c"><ul><li>Lorem ipsum dolor sit amet, consectetur adipiscing elit.</li></ul></div>
      <div class="c"><ul><li>Lorem ipsum dolor sit amet, consectetur adipiscing elit.</li></ul></div>
      <div class="c"><ul><li>Lorem ipsum dolor sit amet, consectetur adipiscing elit.</li></ul></div>
      <div class="c alt"><ul><li>Lorem ipsum dolor sit amet, consectetur adipiscing elit.</li></ul></div>
      <div class="c alt"><ul><li>Lorem ipsum dolor sit amet, consectetur adipiscing elit.</li></ul></div>
      <div class="c alt"><ul><li>Lorem ipsum dolor sit amet, consectetur adipiscing elit.</li></ul></div>
      <div class="c alt"><ul><li>Lorem ipsum dolor sit amet, consectetur adipiscing elit.</li></ul></div>
    </div>
  </div>
  <footer class="foot"><div class="cities">London | Dubai | Melbourne | St. Helier | Sydney<br><span>www.corvelassociates.net</span></div><div class="brand">Corvel Associates <small>Executive search &amp; advisory</small></div></footer>
</section>

<!-- Row 4 -->
<section class="page" style="left:163px;top:2825px">
  <div class="pnum">7</div>
  <div class="inner">
    <h2 class="title">Highlighted Candidates</h2>
    <div class="cand">
      <div class="photo" role="img" aria-label="Portrait photo of candidate"></div>
      <div class="body">
        <div class="name">John Doe</div>
        <div class="badge">Vice President</div>
        <div class="contact"><span>United Kingdom</span><span>info@corvelassociates.co.uk</span><span>+44 200 000 0000</span></div>
        <p>Lorem ipsum dolor sit amet, consectetur adipiscing elit. Vivamus sed ullamcorper libero. Nam cursus ut turpis eu porttitor. Duis sit amet neque ultrices, aliquet mauris non, pulvinar augue. Aenean tellus mi, fermentum in pharetra vitae, semper a est. Duis nec auctor eros. Integer ultrices lectus risus, vitae dapibus tortor varius vel.</p>
        <p>Quisque et pulvinar urna, ut pretium leo. Mauris turpis quam, bibendum at risus in, vestibulum accumsan leo. Donec eu convallis neque. Etiam aliquet, dui at gravida posuere, dui mi pellentesque mi, eget lobortis eros justo ac magna. Mauris euismod gravida dolor in pellentesque.</p>
      </div>
    </div>
    <div class="exp-h">Professional Experience</div>
    <div class="tl">
      <div class="yr">2010</div><div class="ct">Content Here</div>
      <div class="tx">Lorem ipsum dolor sit amet, consectetur adipiscing elit. Vivamus sed ullamcorper libero. Nam cursus ut turpis eu porttitor. Duis sit amet neque ultrices, aliquet mauris non, pulvinar augue.</div>
      <div class="yr">2015</div><div class="ct">Content Here</div>
      <div class="tx"><ul><li>Lorem ipsum dolor sit amet, consectetur adipiscing elit.</li><li>Vivamus sed ullamcorper libero. Nam cursus ut turpis eu porttitor.</li><li>Duis sit amet neque ultrices, aliquet mauris non, pulvinar augue.</li></ul></div>
      <div class="yr">2018</div><div class="ct">Content Here</div>
      <div class="tx"><ul><li>Fusce rhoncus lectus et augue tincidunt tempor.</li><li>Aenean vestibulum nunc ac diam scelerisque, et efficitur ligula pharetra.</li><li>Integer nec felis non neque mattis fermentum.</li><li>Sed egestas et elit placerat commodo at a lorem.</li></ul></div>
      <div class="yr">2018 – Now</div><div class="ct">Content Here</div>
      <div class="tx"><ul><li>Fusce rhoncus lectus et augue tincidunt tempor.</li><li>Aenean vestibulum nunc ac diam scelerisque, et efficitur ligula pharetra. Curabitur vitae est at dolor eleifend pharetra eu non dolor.</li><li>Praesent elementum dui id fringilla sodales.</li></ul></div>
    </div>
  </div>
  <footer class="foot"><div class="cities">London | Dubai | Melbourne | St. Helier | Sydney<br><span>www.corvelassociates.net</span></div><div class="brand">Corvel Associates <small>Executive search &amp; advisory</small></div></footer>
</section>

<section class="page dark" style="left:607px;top:2825px">
  <div class="pnum">8</div>
  <div class="inner body" style="top:64px;left:58px;right:50px">
    <div class="h1" style="font-size:8px;margin-bottom:3px">Image and Text Sample</div>
    <p>Lorem ipsum dolor sit amet, consectetur adipiscing elit. Ut ut quam eu lectus consectetur porttitor. Sed lorem arcu, semper id lorem non, tempus vulputate lacus. Vivamus ex justo, mollis sit amet mollis varius, pellentesque at ligula. Cras elementum consequat massa, nec maximus nibh convallis sit amet. In condimentum rhoncus euismod. Aenean ac imperdiet quam, quis luctus erat non fringilla. Maecenas tempor nibh arcu, eu iaculis purus consequat sit amet.</p>
    <p>Quisque placerat et ipsum at porttitor. Suspendisse quam urna, malesuada ac ante ipsum. Nam porttitor luctus ipsum ut iaculis. Pellentesque hendrerit sapien felis, vel facilisis nibh maximus quis. Ut tincidunt justo turpis, quis dapibus diam facilisis, hendrerit tellus. Donec aliquam dapibus mi, id luctus sem ultrices a. Nunc a lectus sit amet mi iaculis semper. Interdum et primis in faucibus. Nam porttitor dolor id imperdiet cursus. Aliquam et diam pellentesque lorem tempus tempus. Phasellus ut enim volutpat, lacinia mauris tempus, tempus velit.</p>
    <p>Praesent aliquam viverra turpis id elementum. Cras efficitur, risus a dignissim eleifend, magna metus molestie urna, nec porttitor turpis placerat nisi. Nulla placerat in erat id sodales. Phasellus sagittis posuere iaculis. Duis ut porta elit, et consectetur tortor. Mauris ultricies leo quis placerat venenatis. Morbi vitae ultricies quam. Proin feugiat euismod diam, vitae interdum ipsum sodales vel. Nunc eleifend varius est, vel dapibus volutpat. Sed justo pretium ex, ut eget fermentum arcu. Aenean ultricies nec enim at convallis. Vivamus a leo dictum, luctus est ornare, efficitur lorem.</p>
    <ul>
      <li>Vivamus nec rhoncus massa eu libero interdum semper.</li>
      <li>Nunc imperdiet arcu sollicitudin diam vehicula tincidunt.</li>
      <li>Nulla pellentesque rutrum diam, vel blandit neque vulputate porttitor. Nam tempor eu tortor vel rutrum. Mauris dapibus dignissim turpis, at egestas sem mattis quis. Maecenas pulvinar facilisis velit, nec accumsan tellus scelerisque vel.</li>
      <li>Nulla rutrum nunc quis dapibus placerat. Donec quis urna magna. Cras ac tristique ipsum. Sed sed dapibus orci, non pellentesque mauris. Donec sollicitudin nibh et nisl ornare, a aliquet ex convallis. Aliquam erat volutpat.</li>
      <li>Donec malesuada gravida tortor. Id molestie sem convallis vel. Donec placerat libero vitae quam pretium maximus.</li>
      <li>Etiam faucibus condimentum diam sed ornare. Aenean eu mi sem.</li>
      <li>Pellentesque urna ligula, iaculis in dui eu, fringilla congue lorem.</li>
      <li>Vestibulum interdum ipsum at porta vestibulum.</li>
    </ul>
  </div>
  <footer class="foot"><div class="cities">London | Dubai | Melbourne | St. Helier | Sydney<br><span>www.corvelassociates.net</span></div><div class="brand">Corvel Associates <small>Executive search &amp; advisory</small></div></footer>
</section>

<!-- Row 5 -->
<section class="page" style="left:163px;top:3454px">
  <div class="pnum">9</div>
  <div class="inner body" style="top:48px">
    <div class="photo-wide" role="img" aria-label="Photo of the Palace of Westminster and clock tower under a cloudy sky"></div>
    <p>Lorem Ipsum is simply dummy text of the printing and typesetting industry. Lorem Ipsum has been the industry's standard dummy text ever since the 1500s, when an unknown printer took a galley of type and scrambled it to make a type specimen book. It has survived not only five centuries, but also the leap into electronic typesetting, remaining essentially unchanged. It was popularised in the 1960s with the release of sheets containing Lorem Ipsum passages, and more recently with desktop publishing software including versions of Lorem Ipsum.</p>
    <ul style="padding-left:10px">
      <li>Lorem ipsum dolor sit amet, consectetur adipiscing elit (Bullet Style)</li>
      <li>Vestibulum condimentum nisi sed lorem eleifend egestas.
        <ul style="list-style:'- ';padding-left:10px"><li>Maecenas vel metus quis lorem euismod varius. (Sub Bullet Style)</li><li>Cras luctus magna ac diam imperdiet, in tempus felis imperdiet.
          <ul style="list-style:'• ';padding-left:10px"><li>Phasellus id nibh hendrerit quam rhoncus tincidunt. (Sub Bullet 2 Style)</li><li>Aliquam fringilla erat id pulvinar ullamcorper.</li></ul></li></ul></li>
    </ul>
    <div class="quote"><span class="qm">“</span><div style="margin-top:6px"><p>The following clauses must be added to the order form when selected Lorem ipsum dolor sit amet, consectetur</p><span class="qm-end">”</span></div></div>
  </div>
  <footer class="foot"><div class="cities">London | Dubai | Melbourne | St. Helier | Sydney<br><span>www.corvelassociates.net</span></div><div class="brand">Corvel Associates <small>Executive search &amp; advisory</small></div></footer>
</section>

<section class="page thanks" style="left:607px;top:3454px">
  <div class="glow" role="img" aria-label="Faint photo of a lighthouse on a headland in red tones"></div>
  <h2>THANK YOU</h2>
  <div class="brand">Corvel Associates</div>
  <div class="cities">London | Dubai | Melbourne | St. Helier | Sydney<br>www.corvelassociates.net</div>
</section>

</body>
</html>
```